Flyer-Design für Seniorenbetreuung
Zielgruppe
Wir sind eine Genossenschaft, welche ihren Immobilienbestand gern erweitern möchte. Dafür soll für unsere Partnerfirma (welche im Seniorenbetreuungssektor tätig ist) eine Flyer erdacht werden, welcher Senioren bzw. ihre Angehörigen anspricht die Wohneigentum besitzen. Viele Senioren besitzen Ein-, Mehrfamilienhäuser oder Eigentumswohnungen und können oder wollen diese nicht weiter vererben. Zusätzlich sind sie durch die Kosten des Eigentums, wie Steuern oder Instandhaltungskosten belastet. Unsere Genossenschaft bietet eine Lösung des Problems. Eine Übernahme des Eigentums bei gleichzeitigem lebenslangem Wohnrecht. Die Zielgruppe soll in dem Flyer auf die bestehende Probleme angesprochen werden und gleichzeitig eine individuelle Lösung angeboten werden, welche eine Mitgliedschaft in dem sozialen Verbund der Genossenschaft ist.
Aufgabenstellung
Der Designer hat hier völlig freie Hand. Es sollte auf die Zielgruppe passen.
Passende Texte soll sich der Designer selbst erdenken.
Nachtrag: Ich habe mittlerweile viele Zuschriften bekommen, dass die Aufgabenstellung sich Texte auszudenken etwas zu allgemein gefasst ist, daher versuche ich hier nochmal etwas Licht in Dunkle zu bringen. Ich habe genauso wenig eine Idee, wie und mit welcher Wortwahl ein Senior auf einfühlsame Weise darauf angesprochen werden soll, ob er nicht sein Haus verkaufen möchte. Meine bisherigen Ideen waren:
'Haben sie schon einmal über den Verkauf ihrer Immobilie nachgedacht? Wussten sie, dass sie ihr Wohneigentum im vollen Umfang weiter nutzen können, ohne weiter die Kosten tragen zu müssen? Sie wollen wissen wie? Rufen sie doch einfach an und ich werde ihnen genau erklären, welche Vorzüge die Mitgliedschaft in einer Genossenschaft mit sich bringt.'
Allerdings erscheint mir das viel zu direkt und ich finde nicht die richtigen Worte diese Personengruppe in dem Maße anzusprechen, wie es nötig wäre, um sie zu einem Anruf zu bewegen. Daher hatte ich gehofft, dass sie hier ein findiger Designer findet, welcher eine bessere kreative Art hat als ich.
Vielleicht ist es die falsche Plattform, vielleicht schaffen wir es nicht die Vorgaben zu spezifizieren. Bilder anzuordnen ist sicher sehr wichtig, auch ist es wichtig aufhellende Elemente einzubringen. Aber wir suchen jemanden der einen Flyer so gestalten kann das der Flyer etwas ausdrückt, das eine Botschaft vermittelt wird, das auf einem Blick der Senior den Wunsch verspürt, bei uns anzurufen. Das heißt viel wichtiger als Bilder, ist der Inhalt der Ansprache. Nicht unbedingt der Inhalt, sondern das WIE. Nochmal: wir wollen ältere Menschen dazu bewegen ihr Eigentum auf Grund von Reperaturrückstau, Überlastung, gesundheitlichen Einschränkungen, finanziellen Schwierigkeiten, zu großem Aufwand in eine Genossenschaft einzubringen. Ds heißt S..

```html
<!DOCTYPE html>
<html lang="de">
<head>
<meta charset="utf-8">
<title>Domus Concordia – Flyer</title>
<link href="https://fonts.googleapis.com/css2?family=Source+Sans+3:ital,wght@0,400;0,600;0,700;1,700&display=swap" rel="stylesheet">
<style>
  :root {
    --navy: #2a3582;
    --red: #c91a22;
    --green: #43a535;
    --white: #ffffff;
    --stage: #ece8e2;
    --photo-garden: linear-gradient(135deg, #3f6b2a 0%, #7ea24a 45%, #c9c4a8 75%, #e8e6dc 100%);
    --photo-window: linear-gradient(120deg, #5b3c57 0%, #8a6a80 40%, #d9dde0 70%, #f2f4f4 100%);
  }
  * { box-sizing: border-box; margin: 0; padding: 0; }
  html, body { width: 997px; height: 1200px; overflow: hidden; }
  body {
    background: var(--stage);
    font-family: "Source Sans 3", "Myriad Pro", sans-serif;
    position: relative;
  }
  .panel {
    position: absolute;
    top: 48px;
    width: 384px;
    height: 1085px;
    background: var(--white);
    overflow: hidden;
  }
  .panel--problems { left: 78px; }
  .panel--stories { left: 526px; }

  /* Left panel */
  .intro {
    position: absolute; left: 37px; right: 34px; top: 30px;
    color: var(--navy); font-weight: 700; font-size: 18.5px; line-height: 1.27;
    text-align: justify;
  }
  .intro p + p { margin-top: 22px; text-align: left; }
  .section-title {
    position: absolute; left: 37px; right: 30px;
    font-weight: 700; font-size: 18.5px; line-height: 1.27;
  }
  .section-title--red { top: 218px; color: var(--red); }
  .section-title--green { top: 527px; color: var(--green); }
  .pill {
    position: absolute; left: 0; width: 348px;
    border-radius: 0 22px 22px 0;
    color: var(--white); font-weight: 700; font-size: 14.5px; line-height: 1.3;
    padding: 0 26px 0 37px;
    display: flex; align-items: center;
  }
  .pill--red { background: var(--red); }
  .pill--green { background: var(--green); }
  .cta {
    position: absolute; left: 37px; right: 30px; top: 870px;
    color: var(--navy); font-weight: 700; font-size: 15.5px; line-height: 1.35;
  }
  .contact {
    position: absolute; left: 0; right: 0; bottom: 0; height: 160px;
    background: var(--navy); color: var(--white);
    padding: 28px 0 0 65px;
  }
  .contact__name { font-size: 22px; font-weight: 700; line-height: 1.1; }
  .contact__address { font-size: 15px; margin-top: 3px; }
  .contact__phone {
    display: flex; align-items: center; gap: 14px;
    font-size: 32px; font-weight: 700; margin-top: 22px;
  }

  /* Right panel */
  .photo { position: absolute; left: 0; right: 0; }
  .photo--garden { top: 25px; height: 267px; background: var(--photo-garden); }
  .photo--window { top: 567px; height: 236px; background: var(--photo-window); }
  .story {
    position: absolute; left: 0; right: 0; color: var(--white);
    padding: 26px 30px 0 33px;
  }
  .story--green { top: 292px; height: 250px; background: var(--green); }
  .story--blue { top: 803px; height: 282px; background: var(--navy); }
  .story__text {
    font-size: 16px; line-height: 1.38; text-align: justify; position: relative;
    text-indent: 24px;
  }
  .story__text::before {
    content: "\201D"; position: absolute; left: -18px; top: -16px; text-indent: 0;
    font-size: 64px; font-weight: 700; font-style: italic; line-height: 1;
  }
  .story__question {
    font-size: 21px; line-height: 1.3; margin-top: 18px; padding-right: 40px; position: relative;
  }
  .story__question::after {
    content: "\201D"; position: absolute; right: -14px; bottom: -34px;
    font-size: 64px; font-weight: 700; font-style: italic; line-height: 1;
  }
</style>
</head>
<body>
  <section class="panel panel--problems">
    <div class="intro">
      <p>Viele Senioren plagen im Alter Geldsorgen und Ängste was mit dem geschieht, was man sich sein Leben lang aufgebaut hat.</p>
      <p>Gehören Sie auch dazu?<br>Dann wägen Sie einmal ab:</p>
    </div>

    <h2 class="section-title section-title--red">Behalten Sie Ihr/e Haus/Wohnung:</h2>
    <div class="pill pill--red" style="top:256px;height:70px;">Wie bezahlen Sie ein neues Dach / neue Fenster / eine neue Gasheizung etc. bezahlen von Ihrer Rente / ohne Kredit?</div>
    <div class="pill pill--red" style="top:342px;height:70px;">Wie bezahlen Sie dauerhaft die Grundsteuer oder eine anstehende Sanierung in Ihrer Anliegerstraße?</div>
    <div class="pill pill--red" style="top:428px;height:70px;">Wer erbt Ihr Haus / Ihre Wohnung, wenn es keine Kinder / Verwandten gibt die etwas erben könnten / sollen?</div>

    <h2 class="section-title section-title--green">Nach einem Verkauf der Immobilie an unsere Genossenschaft „Domus Concordia“…</h2>
    <div class="pill pill--green" style="top:614px;height:52px;">… können Sie wie bisher in Ihrer Immobilie wohnen - auf Lebenszeit!</div>
    <div class="pill pill--green" style="top:680px;height:70px;">… ändert sich für Sie nur die finanzielle Belastung, die sich deutlich reduzieren wird. Keine Sorgen mehr deswegen.</div>
    <div class="pill pill--green" style="top:765px;height:71px;">… kümmert die Genossenschaft sich um anstehende Renovierungsarbeiten und zahlt Steuern, Anliegerkosten etc.</div>

    <p class="cta">Rufen Sie uns unverbindlich an und wir sprechen über Ihre Möglichkeiten:</p>

    <footer class="contact">
      <div class="contact__name">Domus Concordia</div>
      <div class="contact__address">Lindenweg 8 · 34567 Beispielfeld</div>
      <div class="contact__phone">
        <svg width="32" height="24" viewBox="0 0 32 24" aria-hidden="true">
          <path d="M2 8 Q16 -2 30 8 L27 12 L22 10 L21 6 Q16 4 11 6 L10 10 L5 12 Z" fill="#fff"/>
          <path d="M9 12 L23 12 L28 22 L4 22 Z" fill="#fff"/>
          <circle cx="16" cy="17" r="3" fill="#2a3582"/>
        </svg>
        <span>0987 654321</span>
      </div>
    </footer>
  </section>

  <section class="panel panel--stories">
    <div class="photo photo--garden" role="img" aria-label="Foto: ältere Frau mit Sonnenhut pflegt Rosen in ihrem Garten"></div>
    <div class="story story--green">
      <p class="story__text">Ich bin noch fit genug, um meinen Garten und meinen Haushalt in Schuss zu halten - ich möchte hier nicht ausziehen. Aber seit mein Mann vor zwei Jahren verstorben ist, muss ich mit meiner kleinen Rente und der Witwenrente jeden Cent umdrehen.</p>
      <p class="story__question">Wie kann ich meine Unterhaltungskosten senken?</p>
    </div>

    <div class="photo photo--window" role="img" aria-label="Foto: älteres Ehepaar sitzt nachdenklich am Fenster mit Zimmerpflanzen"></div>
    <div class="story story--blue">
      <p class="story__text">Meine Frau und ich haben unseren Sohn in dieser Wohnung groß gezogen. Bei einem Autounfall kam er vor fünf Jahren ums Leben. Nun wissen wir nicht, was mit unserer Wohnung passieren soll, wenn wir nicht mehr sind. Es gibt keine nahen Angehörigen mehr. Soll jemand fremdes alles erben?</p>
      <p class="story__question">Wie können wir für den Erbfall vorsorgen?</p>
    </div>
  </section>
</body>
</html>
```